Water Safety and Program Info Rack Card

We need a rack card - one side has general water safety information and the other side will have our swim school program information along with a QR code to a form to collect their information. We want to use our new brand colors and fonts as much as possible and try to be in alignment with some of the other style of designs we have on our other branded materials. I have some examples of suggested layout that I like the general idea of but can't quite figure out how to finalize it. Also open to completely new ideas. These rack cards will mainly be displayed in hospitals but also could be in other businesses and used at events. Rack card will be somewhere around 4 x 9 in.

```html
<!DOCTYPE html>
<html lang="en">
<head>
<meta charset="utf-8">
<title>ABC's of Water Safety – Rack Card</title>
<link rel="stylesheet" href="https://fonts.googleapis.com/css2?family=Chewy&family=Lilita+One&family=Poppins:wght@500;600&display=swap">
<style>
  :root {
    --sky-top: #ffffff;
    --sky-bottom: #e3f2f8;
    --water-mid: #1b93b8;
    --water-deep: #0e6a93;
    --panel: #27b4c8;
    --lime: #bccd55;
    --ink-teal: #1a5a73;
    --brand-blue: #3a84c2;
    --brand-green: #8cc63f;
    --partner-teal: #17707c;
    --title-yellow: #f3e23b;
    --title-blue: #1f68a8;
    --white: #ffffff;
  }
  * { box-sizing: border-box; margin: 0; padding: 0; }
  html, body { width: 1200px; height: 2611px; overflow: hidden; }
  body {
    position: relative;
    font-family: "Poppins", sans-serif;
    background: linear-gradient(180deg, var(--sky-top) 0px, var(--sky-bottom) 600px, var(--water-mid) 760px, var(--water-deep) 2611px);
  }
  .abs { position: absolute; }

  /* Header brands */
  .school-brand { left: 132px; top: 150px; display: flex; align-items: center; gap: 26px; }
  .school-brand .dot { width: 90px; height: 90px; border-radius: 50%; background: var(--brand-green); flex: none; }
  .school-brand .name { color: var(--brand-blue); font-weight: 500; font-size: 46px; line-height: 1.15; }
  .partner-brand { left: 860px; top: 150px; display: flex; align-items: center; gap: 20px; }
  .partner-brand .ring { width: 74px; height: 74px; border-radius: 50%; border: 7px solid var(--partner-teal); flex: none; }
  .partner-brand .name { color: var(--partner-teal); font-weight: 600; font-size: 40px; line-height: 1.05; }

  /* Title */
  .title-splash { left: 188px; top: 376px; width: 837px; height: 292px; border-radius: 46% 50% 44% 48% / 55% 50% 52% 48%;
    background: radial-gradient(ellipse at 50% 45%, #ffffff 0%, #eaf7fc 55%, #bfe6f3 100%); }
  .title { left: 188px; top: 400px; width: 837px; text-align: center; font-family: "Lilita One", sans-serif; line-height: 1; font-weight: 400; }
  .title .abc { font-size: 150px; color: var(--title-yellow); -webkit-text-stroke: 4px var(--title-blue); text-shadow: 0 6px 0 var(--title-blue); }
  .title .of { font-size: 54px; color: var(--title-blue); }
  .title .sub { display: block; font-size: 86px; color: var(--title-blue); margin-top: -4px; }

  .water-surface { left: 0; top: 590px; width: 1200px; height: 200px; }

  /* Sections */
  .panel { left: 117px; width: 970px; }
  .panel svg { position: absolute; inset: 0; width: 100%; height: 100%; }
  .panel .content { position: relative; padding: 0 30px 0 48px; }
  .panel .lead { color: var(--ink-teal); font-weight: 600; font-size: 33px; line-height: 48px; text-align: center; padding-right: 18px; }
  .panel ul { list-style: none; margin-top: 12px; }
  .panel li { position: relative; color: var(--white); font-weight: 600; font-size: 30px; line-height: 52px; padding-left: 27px; white-space: nowrap; }
  .panel li::before { content: ""; position: absolute; left: 0; top: 21px; width: 11px; height: 11px; border-radius: 50%; background: var(--white); }

  .tag { left: 600px; transform: translateX(-50%); height: 107px; padding: 0 34px; background: var(--lime);
    display: flex; align-items: center; justify-content: center; white-space: nowrap;
    font-family: "Chewy", "Lilita One", sans-serif; font-size: 66px; color: var(--white); letter-spacing: 1px;
    text-shadow: 2px 3px 0 rgba(26, 90, 115, 0.55); z-index: 2; }
</style>
</head>
<body>

  <div class="abs school-brand">
    <span class="dot"></span>
    <span class="name">Larkin<br>Family Swim School</span>
  </div>
  <div class="abs partner-brand">
    <span class="ring"></span>
    <span class="name">Vale<br>Health</span>
  </div>

  <svg class="abs water-surface" viewBox="0 0 1200 200" preserveAspectRatio="none" aria-hidden="true">
    <defs>
      <linearGradient id="surface" x1="0" y1="0" x2="0" y2="1">
        <stop offset="0" stop-color="#bfe8f3"/>
        <stop offset="0.5" stop-color="#3fbfd6"/>
        <stop offset="1" stop-color="#1b93b8"/>
      </linearGradient>
    </defs>
    <path d="M0 60 C200 20 380 90 600 55 S980 20 1200 50 L1200 200 L0 200 Z" fill="url(#surface)"/>
    <path d="M0 95 C250 70 420 120 640 92 S1000 75 1200 95" fill="none" stroke="#ffffff" stroke-opacity="0.35" stroke-width="6"/>
  </svg>

  <div class="abs title-splash" role="img" aria-label="Water splash cloud illustration behind the title"></div>
  <h1 class="abs title"><span class="abc">ABC's</span> <span class="of">of</span><span class="sub">Water Safety</span></h1>

  <!-- A -->
  <section class="abs panel" style="top:827px;height:471px;">
    <svg viewBox="0 0 1000 500" preserveAspectRatio="none" aria-hidden="true">
      <path fill="var(--panel)" d="M0 20 L40 10 L80 24 L120 6 L170 22 L230 12 L290 26 L350 8 L420 20 L480 10 L560 24 L620 8 L700 22 L760 10 L830 24 L890 8 L950 20 L1000 12 L996 120 L1002 260 L996 400 L1000 488 L960 476 L900 494 L840 480 L780 496 L720 478 L650 492 L590 476 L520 494 L450 480 L380 496 L320 478 L250 492 L180 476 L120 494 L60 480 L0 492 L4 380 L-2 240 L4 110 Z"/>
    </svg>
    <div class="content" style="padding-top:72px;">
      <p class="lead">A grown-up should always be watching.</p>
      <ul>
        <li>Keep constant, eye-to-eye supervision around<br>any water.</li>
        <li>At parties, assign a deaf Water Watcher.</li>
        <li>Floaties are NOT life jackets or supervision.</li>
        <li>Post 911 and your home address where everyone<br>can find them.</li>
      </ul>
    </div>
  </section>
  <div class="abs tag" style="top:739px;">A=ADULT</div>

  <!-- B -->
  <section class="abs panel" style="top:1448px;height:489px;">
    <svg viewBox="0 0 1000 500" preserveAspectRatio="none" aria-hidden="true">
      <path fill="var(--panel)" d="M0 14 L50 24 L100 8 L160 22 L220 10 L280 24 L340 6 L400 20 L470 8 L540 24 L600 10 L670 22 L730 6 L800 22 L860 10 L930 24 L1000 10 L996 130 L1002 270 L996 400 L1000 490 L940 478 L880 494 L820 476 L760 492 L690 478 L630 496 L560 480 L490 494 L420 476 L360 492 L290 478 L230 496 L160 480 L100 492 L40 476 L0 490 L4 370 L-2 230 L4 100 Z"/>
    </svg>
    <div class="content" style="padding-top:55px;">
      <p class="lead">Make a pool area off-limits without you</p>
      <ul>
        <li>Use a sturdy fence and keep gates, doors, and<br>windows locked.</li>
        <li>Check for gaps or climbable spots around the pool</li>
        <li>Empty and store containers that hold water.</li>
        <li>Keep the view to the pool clear and move<br>climbable items away</li>
      </ul>
    </div>
  </section>
  <div class="abs tag" style="top:1369px;">B=BARRIER</div>

  <!-- C -->
  <section class="abs panel" style="top:2078px;height:423px;">
    <svg viewBox="0 0 1000 500" preserveAspectRatio="none" aria-hidden="true">
      <path fill="var(--panel)" d="M0 18 L60 8 L120 24 L180 10 L250 22 L310 6 L380 22 L440 10 L510 24 L580 8 L640 22 L710 10 L770 24 L840 8 L900 20 L1000 10 L996 140 L1002 280 L996 400 L1000 490 L930 476 L870 494 L800 478 L740 494 L670 476 L600 492 L540 478 L470 496 L400 478 L340 494 L270 476 L200 492 L140 478 L70 494 L0 480 L4 360 L-2 220 L4 100 Z"/>
    </svg>
    <div class="content" style="padding-top:85px;">
      <p class="lead">Safety starts with skills.</p>
      <ul>
        <li>Get CPR trained.</li>
        <li>Enroll and keep kids in conistent swim lessons.</li>
        <li>Tokyo proper boating or jet ski safety course.</li>
      </ul>
    </div>
  </section>
  <div class="abs tag" style="top:2000px;">C=CLASSES</div>

</body>
</html>
```